Menu Based Selling

We want a power point telling our story - www.kettlebrookprovisions.com has the info as well as our video posted on the site. I have uploaded two files specific to this - one is more narrative that can be used and the other is an excel file illustrating how a menu would look

```html
<!DOCTYPE html>
<html lang="en">
<head>
<meta charset="utf-8">
<title>Kettlebrook Provisions – Menu Based Selling Presentation</title>
<link href="https://fonts.googleapis.com/css2?family=Montserrat:wght@400;500;600;700&display=swap" rel="stylesheet">
<style>
:root{
  --page:#dcdcdf;
  --white:#ffffff;
  --green:#8dc66c;
  --green-soft:#a9d48d;
  --blue:#4a86c9;
  --navy:#0d1624;
  --ink:#333a40;
  --gray:#6d7277;
  --line:#c9ced3;
}
*{box-sizing:border-box;margin:0;padding:0}
html,body{width:1200px;height:2788px;overflow:hidden}
body{background:var(--page);font-family:"Montserrat",Arial,sans-serif;color:var(--ink);position:relative}

.showcase{position:absolute;left:0;top:0;width:1200px;height:730px;background:var(--page)}
.hero-slide{transform:scale(1.25);transform-origin:0 0}

.slide{position:absolute;width:562px;height:316px;background:var(--white);overflow:hidden}

/* brand */
.brand{display:flex;align-items:center;gap:7px}
.brand-mark{width:18px;height:18px;background:var(--blue)}
.brand-name{font-size:16px;font-weight:500;color:var(--blue);letter-spacing:-.2px}
.brand.small .brand-mark{width:11px;height:11px}
.brand.small .brand-name{font-size:10px}
.brand.light .brand-mark{background:var(--white)}
.brand.light .brand-name{color:var(--white)}

/* title slide */
.slide-head{position:absolute;left:0;top:0;width:562px;height:87px;display:flex;align-items:center;padding:0 24px}
.partner{margin-left:auto;text-align:right;margin-right:8px}
.partner-lead{font-size:9.5px;line-height:10px;color:var(--green);font-weight:500}
.partner ul{list-style:none;font-size:5.6px;line-height:7px;color:var(--ink);margin-top:2px}
.partner li::before{content:"✓ ";color:var(--green)}
.partner-badge{width:50px;height:48px;background:var(--green)}
.hero{position:absolute;left:0;top:87px;width:562px;height:198px}
.hero-text{position:absolute;left:42px;top:116px;color:var(--white)}
.kicker{font-size:16px;font-weight:400}
.hero-text h1{font-size:35px;line-height:39px;font-weight:600;margin-top:4px;letter-spacing:-.3px}
.date-pill{display:inline-block;margin-top:16px;width:142px;height:17px;line-height:17px;text-align:center;font-size:6.5px;color:var(--white);background:var(--green)}
.date-pill.blue{background:var(--blue)}
.slide-url{position:absolute;left:0;bottom:10px;width:100%;text-align:center;font-size:6.5px;color:var(--ink)}
.slide-url b{font-weight:700}

.v-navy .hero{background:linear-gradient(90deg,#06090f 0%,#142238 38%,#2c4157 58%,#a9432c 78%,#c8622e 86%,#5f6f4a 100%)}
.v-wood .hero{background:linear-gradient(90deg,#06090f 0%,#16263a 35%,#42553d 60%,#6f7a4e 78%,#b8512f 92%,#d9cfa0 100%)}
.v-green .hero{background:linear-gradient(90deg,#9acb7b 0%,#8bbf72 40%,#7aa565 60%,#b75e3a 82%,#7d8f5f 100%)}
.v-blue .hero{background:linear-gradient(90deg,#4b86c7 0%,#5a8fb7 40%,#6f9a80 65%,#8f9966 85%,#d5cc9e 100%)}
.v-brown .hero{background:linear-gradient(90deg,#1e1a15 0%,#2d271f 40%,#4d4233 65%,#6b5c47 85%,#d2c6a4 100%)}

/* content slides */
.slide-title{position:absolute;left:0;top:22px;width:100%;text-align:center;font-size:21px;font-weight:400;color:var(--gray)}
.page-no{position:absolute;right:12px;bottom:10px;width:12px;height:12px;background:var(--green);color:var(--white);font-size:6px;line-height:12px;text-align:center}
.slide-foot-brand{position:absolute;left:16px;bottom:16px}

.features{position:absolute;left:0;top:148px;width:100%;display:flex;justify-content:space-around;padding:0 10px}
.feature{width:160px;text-align:center}
.feature-icon{width:42px;height:42px;border-radius:50%;background:var(--blue);border:3px solid var(--white);margin:0 auto;display:flex;align-items:center;justify-content:center}
.feature h3{font-size:13px;font-weight:400;color:var(--green);margin-top:10px}
.feature p{font-size:6.2px;line-height:7.4px;color:var(--gray);margin-top:6px}

.about-a .band{position:absolute;left:0;top:62px;width:562px;height:108px;background:linear-gradient(90deg,#c24628 0%,#d7742d 18%,#6d8a45 32%,#3c4a40 55%,#1a2330 100%)}
.about-b .band{position:absolute;left:0;top:0;width:562px;height:158px;background:linear-gradient(90deg,#d96a1f 0%,#e0952f 16%,#6d7a3c 30%,#585c5e 55%,#3a3e44 100%)}
.about-b .slide-title{color:var(--white)}
.about-b .features{top:136px}

.side-panel{position:absolute;left:0;top:0;width:187px;height:316px;background:linear-gradient(180deg,#9ccc7e 0%,#8fc273 55%,#a6d18b 100%)}
.quote{position:absolute;left:12px;top:62px;width:163px;text-align:center;color:var(--white);font-size:17px;line-height:20.5px;font-weight:400}
.quote b{font-weight:600}
.side-panel .slide-foot-brand{left:14px}
.columns{position:absolute;left:205px;top:48px;width:342px;display:flex;gap:16px}
.columns div{width:163px}
.columns p{font-size:6.3px;line-height:7.3px;color:var(--gray);margin-bottom:6px}

.sample{position:absolute;inset:0;background:linear-gradient(90deg,#c2b588 0%,#8a6f4c 10%,#3e3427 24%,#2f2a22 55%,#3c3326 100%)}
.sample-text{position:absolute;left:165px;top:78px;width:390px;text-align:center;color:var(--white)}
.sample-text .lead{font-size:15px}
.sample-text h2{font-size:18px;line-height:20px;font-weight:500;color:var(--green);margin-top:6px}
.sample-text .meta{font-size:11.5px;line-height:12.5px;margin-top:14px}
.sample-text .org{font-size:18px;font-weight:500;color:var(--green);margin-top:9px}

.week-label{position:absolute;left:0;top:118px;width:187px;text-align:center;color:var(--white)}
.week-label span{display:block;font-size:13px}
.week-label strong{display:block;font-size:28px;font-weight:400;margin-top:2px}

.menu{position:absolute;left:202px;top:18px;width:346px;border-collapse:collapse;font-size:4.6px;color:var(--ink)}
.menu th{background:var(--blue);color:var(--white);font-weight:600;font-size:6px;height:11px;text-align:left;padding-left:8px}
.menu td{height:8.3px;padding:0 6px;border-bottom:.5px solid #e1e4e7}
.menu td.meal{font-size:11.5px;color:var(--gray);width:117px;padding-left:5px;border-bottom:0}
.menu td.cost{width:115px}
.menu tr.total td{background:var(--green-soft);color:var(--white);font-weight:600}
.menu tr.grand td{background:var(--blue);color:var(--white);font-weight:600;height:10px;font-size:5.5px}

.contact-hero{position:absolute;left:0;top:87px;width:562px;height:198px;background:linear-gradient(90deg,#0b1522 0%,#14243a 40%,#2f4b6c 70%,#6f8eac 85%,#233a55 100%)}
.contact-text{position:absolute;left:48px;top:115px;color:var(--white)}
.contact-text h2{font-size:14px;font-weight:600}
.contact-text address{font-style:normal;font-size:7.5px;line-height:9px;margin-top:4px}
.contact-list{list-style:none;margin-top:14px;font-size:7.5px}
.contact-list li{display:flex;align-items:center;gap:8px;height:16px}
</style>
</head>
<body>

<section class="showcase">
  <div class="slide v-navy hero-slide" style="left:249px;top:170px">
    <header class="slide-head">
      <div class="brand"><span class="brand-mark"></span><span class="brand-name">Kettlebrook Provisions</span></div>
      <div class="partner">
        <p class="partner-lead">As a Child Meal Program<br>Partner, We Now Offer:</p>
        <ul><li>Meal Pattern Review by Dietitian</li><li>PFS &amp; CN Labels</li><li>Program Product List from Distributor</li></ul>
      </div>
      <span class="partner-badge"></span>
    </header>
    <div class="hero" role="img" aria-label="Fresh tomatoes and salad greens on a dark background"></div>
    <div class="hero-text"><p class="kicker">Kettlebrook Provisions</p><h1>Presentation Title<br>Goes Here!</h1><span class="date-pill">Tuesday, March 1, 2022</span></div>
    <footer class="slide-url">https://www.<b>kettlebrookprovisions</b>.com/</footer>
  </div>
</section>

<!-- title variants -->
<div class="slide v-navy" style="left:28px;top:766px">
  <header class="slide-head">
    <div class="brand"><span class="brand-mark"></span><span class="brand-name">Kettlebrook Provisions</span></div>
    <div class="partner"><p class="partner-lead">As a Child Meal Program<br>Partner, We Now Offer:</p><ul><li>Meal Pattern Review by Dietitian</li><li>PFS &amp; CN Labels</li><li>Program Product List from Distributor</li></ul></div>
    <span class="partner-badge"></span>
  </header>
  <div class="hero" role="img" aria-label="Fresh tomatoes and salad greens on a dark background"></div>
  <div class="hero-text"><p class="kicker">Kettlebrook Provisions</p><h1>Presentation Title<br>Goes Here!</h1><span class="date-pill">Tuesday, March 1, 2022</span></div>
  <footer class="slide-url">https://www.<b>kettlebrookprovisions</b>.com/</footer>
</div>

<div class="slide v-wood" style="left:609px;top:766px">
  <header class="slide-head">
    <div class="brand"><span class="brand-mark"></span><span class="brand-name">Kettlebrook Provisions</span></div>
    <div class="partner"><p class="partner-lead">As a Child Meal Program<br>Partner, We Now Offer:</p><ul><li>Meal Pattern Review by Dietitian</li><li>PFS &amp; CN Labels</li><li>Program Product List from Distributor</li></ul></div>
    <span class="partner-badge"></span>
  </header>
  <div class="hero" role="img" aria-label="Tomatoes and potatoes on a wooden table"></div>
  <div class="hero-text"><p class="kicker">Kettlebrook Provisions</p><h1>Presentation Title<br>Goes Here!</h1><span class="date-pill blue">Tuesday, March 1, 2022</span></div>
  <footer class="slide-url">https://www.<b>kettlebrookprovisions</b>.com/</footer>
</div>

<div class="slide v-green" style="left:28px;top:1101px">
  <header class="slide-head">
    <div class="brand"><span class="brand-mark"></span><span class="brand-name">Kettlebrook Provisions</span></div>
    <div class="partner"><p class="partner-lead">As a Child Meal Program<br>Partner, We Now Offer:</p><ul><li>Meal Pattern Review by Dietitian</li><li>PFS &amp; CN Labels</li><li>Program Product List from Distributor</li></ul></div>
    <span class="partner-badge"></span>
  </header>
  <div class="hero" role="img" aria-label="Fresh tomatoes and salad greens under a green tint"></div>
  <div class="hero-text"><p class="kicker">Kettlebrook Provisions</p><h1>Presentation Title<br>Goes Here!</h1><span class="date-pill blue">Tuesday, March 1, 2022</span></div>
  <footer class="slide-url">https://www.<b>kettlebrookprovisions</b>.com/</footer>
</div>

<div class="slide v-blue" style="left:609px;top:1101px">
  <header class="slide-head">
    <div class="brand"><span class="brand-mark"></span><span class="brand-name">Kettlebrook Provisions</span></div>
    <div class="partner"><p class="partner-lead">As a Child Meal Program<br>Partner, We Now Offer:</p><ul><li>Meal Pattern Review by Dietitian</li><li>PFS &amp; CN Labels</li><li>Program Product List from Distributor</li></ul></div>
    <span class="partner-badge"></span>
  </header>
  <div class="hero" role="img" aria-label="Potatoes on a wooden table under a blue tint"></div>
  <div class="hero-text"><p class="kicker">Kettlebrook Provisions</p><h1>Presentation Title<br>Goes Here!</h1><span class="date-pill">Tuesday, March 1, 2022</span></div>
  <footer class="slide-url">https://www.<b>kettlebrookprovisions</b>.com/</footer>
</div>

<div class="slide v-brown" style="left:28px;top:1436px">
  <header class="slide-head">
    <div class="brand"><span class="brand-mark"></span><span class="brand-name">Kettlebrook Provisions</span></div>
    <div class="partner"><p class="partner-lead">As a Child Meal Program<br>Partner, We Now Offer:</p><ul><li>Meal Pattern Review by Dietitian</li><li>PFS &amp; CN Labels</li><li>Program Product List from Distributor</li></ul></div>
    <span class="partner-badge"></span>
  </header>
  <div class="hero" role="img" aria-label="Potatoes on a dark wooden table"></div>
  <div class="hero-text"><p class="kicker">Kettlebrook Provisions</p><h1>Presentation Title<br>Goes Here!</h1><span class="date-pill">Tuesday, March 1, 2022</span></div>
  <footer class="slide-url">https://www.<b>kettlebrookprovisions</b>.com/</footer>
</div>

<!-- about us A -->
<div class="slide about-a" style="left:609px;top:1436px">
  <h2 class="slide-title">About Us</h2>
  <div class="band" role="img" aria-label="Tomatoes and greens on a dark surface"></div>
  <div class="features">
    <div class="feature">
      <div class="feature-icon"><svg width="16" height="16" viewBox="0 0 16 16"><circle cx="8" cy="6" r="4.5" fill="none" stroke="#fff" stroke-width="1.4"/><rect x="6" y="11" width="4" height="3" fill="#fff"/></svg></div>
      <h3>Who We Are</h3>
      <p>Kettlebrook Provisions is a one-stop food, services and supply partner to for-profit and nonprofit, social and human service sector organizations throughout the United States.</p>
    </div>
    <div class="feature">
      <div class="feature-icon"><svg width="18" height="16" viewBox="0 0 18 16"><circle cx="6" cy="9" r="4.5" fill="none" stroke="#fff" stroke-width="1.4"/><circle cx="13" cy="5" r="3" fill="none" stroke="#fff" stroke-width="1.4"/></svg></div>
      <h3>Who We Serve</h3>
      <p>For-profit, nonprofit, and social/human service organizations. Helping you spend your dollars on what matters most: your mission and direct service activities.</p>
    </div>
    <div class="feature">
      <div class="feature-icon"><svg width="14" height="16" viewBox="0 0 14 16"><rect x="1.5" y="1" width="11" height="14" fill="none" stroke="#fff" stroke-width="1.4"/><path d="M4 5h6M4 8h6M4 11h4" stroke="#fff" stroke-width="1.2"/></svg></div>
      <h3>Get Started Now</h3>
      <p>All you have to do is register with us. Our professionals will perform an audit of your organization's food and supply purchases based on the invoices that you provide.</p>
    </div>
  </div>
  <div class="slide-foot-brand brand small"><span class="brand-mark"></span><span class="brand-name">Kettlebrook Provisions</span></div>
  <span class="page-no">6</span>
</div>

<!-- about us B -->
<div class="slide about-b" style="left:28px;top:1771px">
  <div class="band" role="img" aria-label="Orange bell pepper on a gray surface"></div>
  <h2 class="slide-title">About Us</h2>
  <div class="features">
    <div class="feature">
      <div class="feature-icon"><svg width="16" height="16" viewBox="0 0 16 16"><circle cx="8" cy="6" r="4.5" fill="none" stroke="#fff" stroke-width="1.4"/><rect x="6" y="11" width="4" height="3" fill="#fff"/></svg></div>
      <h3>Who We Are</h3>
      <p>Kettlebrook Provisions is a one-stop food, services and supply partner to for-profit and nonprofit, social and human service sector organizations throughout the United States.</p>
    </div>
    <div class="feature">
      <div class="feature-icon"><svg width="18" height="16" viewBox="0 0 18 16"><circle cx="6" cy="9" r="4.5" fill="none" stroke="#fff" stroke-width="1.4"/><circle cx="13" cy="5" r="3" fill="none" stroke="#fff" stroke-width="1.4"/></svg></div>
      <h3>Who We Serve</h3>
      <p>For-profit, nonprofit, and social/human service organizations. Helping you spend your dollars on what matters most: your mission and direct service activities.</p>
    </div>
    <div class="feature">
      <div class="feature-icon"><svg width="14" height="16" viewBox="0 0 14 16"><rect x="1.5" y="1" width="11" height="14" fill="none" stroke="#fff" stroke-width="1.4"/><path d="M4 5h6M4 8h6M4 11h4" stroke="#fff" stroke-width="1.2"/></svg></div>
      <h3>Get Started Now</h3>
      <p>All you have to do is register with us. Our professionals will perform an audit of your organization's food and supply purchases based on the invoices that you provide.</p>
    </div>
  </div>
  <div class="slide-foot-brand brand small"><span class="brand-mark"></span><span class="brand-name">Kettlebrook Provisions</span></div>
  <span class="page-no">7</span>
</div>

<!-- narrative -->
<div class="slide" style="left:609px;top:1771px">
  <div class="side-panel" role="img" aria-label="Fresh vegetables under a green tint">
    <p class="quote">It is not the price of <b>“Green Beans”</b> that you should be concerned about - it is the price for the meal.</p>
    <div class="slide-foot-brand brand small light"><span class="brand-mark"></span><span class="brand-name">Kettlebrook Provisions</span></div>
  </div>
  <div class="columns">
    <div>
      <p>With Kettlebrook Provisions' dynamic menu creation process we can help create meals that meet your budget.</p>
      <p>You can use our standard priced menus and pick and chose by day of week – meal selection to meet your budget. If you are trying to hit a target price on a weekly basis - the daily costs can vary as long as the week balances.</p>
      <p>Are you working within the Child Meal Program or NSPL reimbursement guidelines and wanting to offer creative, fun and tasty food to the children you serve - we can help?</p>
      <p>Whether you have a ready-to-serve requirement of made-from-scratch kitchen we can work with you to design a menu that meets your nutritional requirements but the monetary ones as well.</p>
      <p>So many kitchen cooks/orders are looking at the line-item cost of each item that does not tell the whole story.</p>
    </div>
    <div>
      <p>With our system we look at the meal and show the costs at that level. We will provide recipes, nutritional analysis and guidance on how to save. Our program working with top food distributors throughout the US allows us to offer great pricing and services.</p>
      <p>No matter if your budget is $4 per day or $10 per day, we will devise a budget plan that works for you.</p>
      <p>The process is simple – we identify your weekly budget, what meals you are serving (breakfast, lunch, snack(s) and/or dinner) we talk about your capabilities as it relates to preparation and then we go from there.</p>
      <p>As we are building out your menu we will get you setup with our distributor partners, start building order guides and training your staff on how to place orders.</p>
      <p>All our menus are approved by our Registered Dietitian.</p>
    </div>
  </div>
  <span class="page-no">8</span>
</div>

<!-- sample -->
<div class="slide" style="left:28px;top:2106px">
  <div class="sample" role="img" aria-label="Potatoes and tomatoes on a dark wooden table"></div>
  <div class="sample-text">
    <p class="lead">SAMPLE!</p>
    <h2>WEEK VIEW RESIDENTIAL<br>PROGRAM</h2>
    <p class="meta">March 2022<br>Breakfast, Snack, Lunch and Dinner<br>priced Menu prepared exclusively for</p>
    <p class="org">"Your Organization"</p>
  </div>
  <div class="slide-foot-brand brand small light"><span class="brand-mark"></span><span class="brand-name">Kettlebrook Provisions</span></div>
  <span class="page-no">9</span>
</div>

<!-- Monday -->
<div class="slide" style="left:609px;top:2106px">
  <div class="side-panel" role="img" aria-label="Fresh vegetables under a green tint">
    <div class="week-label"><span>Week #1</span><strong>Monday</strong></div>
    <div class="slide-foot-brand brand small light"><span class="brand-mark"></span><span class="brand-name">Kettlebrook Provisions</span></div>
  </div>
  <table class="menu">
    <tr><th></th><th>Selection</th><th>Cost</th></tr>
    <tr><td class="meal" rowspan="4">Breakfast</td><td>Milk</td><td class="cost">$ 0.31</td></tr>
    <tr><td>Margarine</td><td class="cost">$ 0.01</td></tr>
    <tr><td>Peaches Diced</td><td class="cost">$ 0.37</td></tr>
    <tr><td>Bread WG</td><td class="cost">$ 0.09</td></tr>
    <tr class="total"><td></td><td>Total Breakfast</td><td class="cost">$ 0.78</td></tr>
    <tr><td class="meal" rowspan="3">Snack</td><td>Yogurt, Vanilla</td><td class="cost">$ 0.19</td></tr>
    <tr><td>Kiwi Sliced</td><td class="cost">$ 2.58</td></tr>
    <tr><td>-</td><td class="cost">-</td></tr>
    <tr class="total"><td></td><td>Total Snack</td><td class="cost">$ 2.77</td></tr>
    <tr><td class="meal" rowspan="6">Lunch</td><td>Water</td><td class="cost">$ 0.01</td></tr>
    <tr><td>Turkey and Cheese Hero</td><td class="cost">$ 1.18</td></tr>
    <tr><td>Lettuce and Tomato</td><td class="cost">$ 0.21</td></tr>
    <tr><td>Pickle Spear</td><td class="cost">$ 0.06</td></tr>
    <tr><td>Diced Pear</td><td class="cost">$ 0.37</td></tr>
    <tr><td>Carrot Stick</td><td class="cost">$ 0.13</td></tr>
    <tr class="total"><td></td><td>Total Lunch</td><td class="cost">$ 1.96</td></tr>
    <tr><td class="meal" rowspan="8">Dinner</td><td>Milk</td><td class="cost">$ 0.31</td></tr>
    <tr><td>Salisbury Steak</td><td class="cost">$ 1.33</td></tr>
    <tr><td>Tropical Fruit Salad</td><td class="cost">$ 0.27</td></tr>
    <tr><td>Rice Pilaf</td><td class="cost">$ 0.04</td></tr>
    <tr><td>Peas and Carrots</td><td class="cost">$ 0.12</td></tr>
    <tr><td>Whole Wheat Dinner Roll</td><td class="cost">$ 0.34</td></tr>
    <tr><td>-</td><td class="cost">-</td></tr>
    <tr><td>-</td><td class="cost">-</td></tr>
    <tr class="total"><td></td><td>Total Dinner</td><td class="cost">$ 2.41</td></tr>
    <tr class="grand"><td>Total Day Week #1</td><td></td><td class="cost">$ 7.92</td></tr>
  </table>
  <span class="page-no">10</span>
</div>

<!-- Tuesday -->
<div class="slide" style="left:28px;top:2441px">
  <div class="side-panel" role="img" aria-label="Fresh vegetables under a green tint">
    <div class="week-label"><span>Week #1</span><strong>Tuesday</strong></div>
    <div class="slide-foot-brand brand small light"><span class="brand-mark"></span><span class="brand-name">Kettlebrook Provisions</span></div>
  </div>
  <table class="menu">
    <tr><th></th><th>Selection</th><th>Cost</th></tr>
    <tr><td class="meal" rowspan="4">Breakfast</td><td>Milk</td><td class="cost">$ 0.31</td></tr>
    <tr><td>Hot Oatmeal</td><td class="cost">$ 0.12</td></tr>
    <tr><td>Strawberry Fruit</td><td class="cost">$ 0.19</td></tr>
    <tr><td>-</td><td class="cost">-</td></tr>
    <tr class="total"><td></td><td>Total Breakfast</td><td class="cost">$ 0.62</td></tr>
    <tr><td class="meal" rowspan="3">Snack</td><td>Graham Crackers, PKG</td><td class="cost">$ 0.13</td></tr>
    <tr><td>Honeydew Melon Chunks</td><td class="cost">$ 0.49</td></tr>
    <tr><td>-</td><td class="cost">-</td></tr>
    <tr class="total"><td></td><td>Total Snack</td><td class="cost">$ 0.62</td></tr>
    <tr><td class="meal" rowspan="6">Lunch</td><td>Water</td><td class="cost">$ 0.01</td></tr>
    <tr><td>Sweet and Sour Chicken</td><td class="cost">$ 0.67</td></tr>
    <tr><td>Brown Rice</td><td class="cost">$ 0.08</td></tr>
    <tr><td>California Blend</td><td class="cost">$ 0.21</td></tr>
    <tr><td>Mandarin Oranges</td><td class="cost">$ 0.27</td></tr>
    <tr><td>Whole Wheat Dinner Roll</td><td class="cost">$ 0.34</td></tr>
    <tr class="total"><td></td><td>Total Lunch</td><td class="cost">$ 1.58</td></tr>
    <tr><td class="meal" rowspan="8">Dinner</td><td>Milk</td><td class="cost">$ 0.31</td></tr>
    <tr><td>Italian Sausage</td><td class="cost">$ 0.58</td></tr>
    <tr><td>Fruit Cocktail</td><td class="cost">$ 0.22</td></tr>
    <tr><td>Whole Grain Penne Pasta</td><td class="cost">$ 0.12</td></tr>
    <tr><td>Tomato Sauce</td><td class="cost">$ 0.16</td></tr>
    <tr><td>Peppers and Onions</td><td class="cost">$ 0.05</td></tr>
    <tr><td>Green Beans</td><td class="cost">$ 0.12</td></tr>
    <tr><td>Whole Wheat Dinner Roll</td><td class="cost">$ 0.34</td></tr>
    <tr class="total"><td></td><td>Total Dinner</td><td class="cost">$ 1.90</td></tr>
    <tr class="grand"><td>Total Day Week #1</td><td></td><td class="cost">$ 4.72</td></tr>
  </table>
  <span class="page-no">11</span>
</div>

<!-- contact -->
<div class="slide" style="left:609px;top:2441px">
  <header class="slide-head">
    <div class="brand"><span class="brand-mark"></span><span class="brand-name">Kettlebrook Provisions</span></div>
  </header>
  <div class="contact-hero" role="img" aria-label="Glass office towers seen from below"></div>
  <div class="contact-text">
    <h2>Contact Us</h2>
    <address>380 Millrace Road<br>Brookfield, MA 01506</address>
    <ul class="contact-list">
      <li><svg width="9" height="9" viewBox="0 0 10 10"><path d="M2 1l2 2-1 1.5c.8 1.4 1.6 2.2 3 3L7.5 6l2 2-1.5 1.5C4.5 9 1 5.5.5 2.5z" fill="#fff"/></svg>866-555-0142</li>
      <li><svg width="9" height="9" viewBox="0 0 10 10"><circle cx="5" cy="5" r="4" fill="none" stroke="#fff" stroke-width="1.2"/><circle cx="5" cy="5" r="1.6" fill="none" stroke="#fff" stroke-width="1.1"/></svg>info@kettlebrookprovisions.com</li>
      <li><svg width="9" height="9" viewBox="0 0 10 10"><circle cx="5" cy="5" r="4" fill="none" stroke="#fff" stroke-width="1"/><ellipse cx="5" cy="5" rx="1.8" ry="4" fill="none" stroke="#fff" stroke-width=".8"/><path d="M1 5h8" stroke="#fff" stroke-width=".8"/></svg>www.kettlebrookprovisions.com</li>
    </ul>
  </div>
  <footer class="slide-url">https://www.<b>kettlebrookprovisions</b>.com/</footer>
</div>

</body>
</html>
```